Long Established Local Fencing (not swords) Business needs fresh Business Cards

We need fresh double sided business cards for our Fencing Construction business, we are looking for something with our new logo design added, and maybe a photo background ?
We recently had cards made from Cardlyne and we were horrified with what we got back, the quality was terrible, so am looking for high quality format for good printing company to make.
We install Steelmora, Timber paling, Aluminium Slat Screening, Picket (timber and aluminium) and most other fencing installations.
Our website is brankelrails.com.au should you like to learn a bit more.
We do have logo in other formats if required.
We have been in business for over 35 years and we have used this as a "motto" it is on our signage

Industry/Entity Type

Construction

Contact Information for Business Card

Open to ideas, we need 3 x different cards, one generic with no name and 2 x others each with 1 of our bosses name on each, I will put into upload files.

Colors
ec1f27
000000
606060
f5f5f5

Requirements
Must have
• Company Name and Logo
• Address
• Contact details, phone, website, email etc
• Small space to write notes when leaving card at residence
Nice to have
• Our motto "Servicing the Peninsula for over 35 years"

```html
<!DOCTYPE html>
<html lang="en">
<head>
<meta charset="utf-8">
<title>Brankel Rails – Business Cards</title>
<link rel="stylesheet" href="https://fonts.googleapis.com/css2?family=Open+Sans:wght@700;800&family=Tinos:wght@400;700&family=Roboto+Condensed:wght@800&display=swap">
<style>
  :root {
    --page: #ffffff;
    --stage: #b3b3b3;
    --navy: #03037d;
    --red: #ec1f27;
    --black: #000000;
    --grey: #606060;
    --white: #ffffff;
    --photo-top: #6f8fae;
    --photo-mid: #2f4763;
    --photo-low: #27374f;
  }
  * { margin: 0; padding: 0; box-sizing: border-box; }
  html, body { width: 1200px; height: 980px; overflow: hidden; background: var(--page); }
  .stage {
    position: absolute; left: 17px; top: 17px; width: 1156px; height: 938px;
    background: var(--stage); border: 1px solid #9a9a9a;
  }
  .card {
    position: absolute; left: 355px; width: 515px; overflow: hidden;
    box-shadow: -22px 10px 8px rgba(0,0,0,0.55);
  }
  .card-front { top: 169px; height: 308px; background: var(--navy); }
  .card-back { top: 534px; height: 317px; background: var(--white); }

  .site-photo {
    position: absolute; left: 0; top: 0; width: 515px; height: 166px;
    background: linear-gradient(180deg, var(--photo-top) 0%, #50708f 35%, var(--photo-mid) 45%, var(--photo-low) 100%);
  }
  .portrait-slot {
    position: absolute; left: 46px; top: 98px; width: 114px; height: 114px;
    border-radius: 50%; background: var(--white); border: 4px solid var(--navy);
    font: 400 11px 'Tinos', serif; color: var(--black);
    display: flex; align-items: center; justify-content: center; padding-bottom: 8px;
  }
  .front-brand {
    position: absolute; left: 270px; top: 72px; width: 130px; text-align: center;
    font: 800 15px 'Roboto Condensed', sans-serif; color: var(--white); letter-spacing: 0.5px;
  }
  .holder-name {
    position: absolute; left: 183px; top: 132px;
    font: 700 32px 'Open Sans', sans-serif; color: var(--white); letter-spacing: 0.3px;
  }
  .licence {
    position: absolute; left: 160px; top: 169px; width: 349px;
    display: flex; align-items: center; gap: 8px;
    font: 400 17px 'Tinos', serif; color: var(--white); white-space: nowrap;
  }
  .licence::before, .licence::after { content: ""; flex: 1; height: 2px; background: var(--white); }
  .contact {
    position: absolute; top: 199px;
    font: 700 9.5px/11px 'Tinos', serif; color: var(--white); letter-spacing: 0.6px; white-space: nowrap;
  }
  .contact-left { left: 144px; }
  .contact-right { left: 314px; }
  .contact span { display: inline-block; }
  .contact-left span { width: 40px; }
  .contact-right span { width: 44px; }
  .motto-strip {
    position: absolute; left: 0; top: 253px; width: 515px; height: 28px; background: var(--white);
    display: flex; align-items: center; justify-content: center;
    font: 700 15px 'Tinos', serif; color: var(--red); letter-spacing: 0.4px;
  }

  .back-brand {
    position: absolute; left: 0; top: 124px; width: 515px;
    display: flex; align-items: center; justify-content: center; gap: 10px;
    font: 800 30px 'Roboto Condensed', sans-serif; color: var(--black); letter-spacing: 1px;
  }
  .back-brand .mark { width: 18px; height: 18px; background: var(--red); }
  .notes { position: absolute; left: 29px; top: 234px; width: 458px; }
  .notes-label { position: absolute; left: 1px; top: 0; font: 400 10px 'Tinos', serif; color: var(--black); }
  .note-line { position: absolute; left: 0; width: 458px; height: 1px; background: var(--black); }
</style>
</head>
<body>
  <div class="stage"></div>

  <section class="card card-front">
    <div class="site-photo" role="img" aria-label="Photo of a dark blue steel panel fence with slatted top in front of suburban houses and palm trees"></div>
    <div class="front-brand">BRANKEL RAILS</div>
    <div class="portrait-slot">PHOTO</div>
    <h1 class="holder-name">DARREN KELLOW</h1>
    <div class="licence">GOLD LICENSE No. 48271c</div>
    <div class="contact contact-left">
      <div>Adress: 27 Kerran St Brankel</div>
      <div><span>Ph:</span>43-528164</div>
      <div>PO Box 512 Marlow NSW 2250</div>
    </div>
    <div class="contact contact-right">
      <div><span>Office :</span>(02)43528164</div>
      <div><span>Mobile:</span>0421 736 408</div>
      <div><span>E-mai:</span>brankelrails@netmail.com</div>
      <div><span>Web:</span>www.brankelrails.com.au</div>
    </div>
    <div class="motto-strip">-Make your Business &amp; Life to a better place-</div>
  </section>

  <section class="card card-back">
    <div class="back-brand"><span class="mark"></span>BRANKEL RAILS</div>
    <div class="notes">
      <div class="notes-label">Note :</div>
      <div class="note-line" style="top:14px"></div>
      <div class="note-line" style="top:30px"></div>
      <div class="note-line" style="top:46px"></div>
      <div class="note-line" style="top:62px"></div>
    </div>
  </section>
</body>
</html>
```